Company Brochure / Sales Sheet

We would like a brochure that we will may print out as well as forward electronically to our prospective clients.

Our clients are inventors/doctors/surgeons of medical products who need help completing their medical product, gaining approval, and then selling their product into the US market

Target Market(s)

Inventors of medical products who want to sell them in the United States

Industry/Entity Type

Medical

Font styles to use
Serif
Sans Serif

Requirements
Must have
• The word "Medical" should not receive special empahsis.
• Use the last two photos and whatever other photos that look good. You can edit and crop the photos
• Text should be easy to read
Nice to have
• We want to show that we have a lot of products.
• Sharp, clean, modern
• Minimum two pages - final product should be capable of being printed and
• forwarded electronically
• Easy to read
Should not have
• Should not be cluttered

```html
<!DOCTYPE html>
<html lang="en">
<head>
<meta charset="utf-8">
<title>Halvorsen Health Network – Brochure 2016</title>
<link rel="stylesheet" href="https://fonts.googleapis.com/css2?family=Montserrat:wght@400;600&family=Open+Sans:wght@400&display=swap">
<style>
  :root {
    --bg: #dcdcdc;
    --purple-deep: #3e1f6b;
    --purple: #5a3190;
    --purple-mid: #7a52b0;
    --purple-soft: #b89ad8;
    --map-blue: #6f8fd6;
    --paper: #ffffff;
    --paper-grey: #ebeaee;
    --ink: #3a3a3a;
    --ink-soft: #6a6a6a;
    --black: #111111;
    --swoosh-grey: #b9b9bf;
  }
  * { margin: 0; padding: 0; box-sizing: border-box; }
  html, body { width: 1200px; height: 836px; overflow: hidden; background: var(--bg); }
  .spread { position: relative; width: 1200px; height: 836px; }
  .page {
    position: absolute; top: 36px; width: 540px; height: 764px;
    background: var(--paper); overflow: hidden;
    box-shadow: 0 6px 24px rgba(0,0,0,.18);
  }
  .page--cover { left: 50px; }
  .page--inside { left: 610px; }
  .page svg.page__art { position: absolute; inset: 0; width: 100%; height: 100%; }

  .brand {
    position: absolute; left: 0; right: 0; top: 200px;
    display: flex; flex-direction: column; align-items: center; gap: 12px;
    font-family: "Montserrat", sans-serif; font-weight: 600; color: var(--paper);
  }
  .brand__dot { width: 44px; height: 44px; border-radius: 50%; background: var(--paper); }
  .brand__name { font-size: 22px; letter-spacing: 1px; text-align: center; line-height: 1.35; }
  .brand__name span { display: block; font-size: 22px; letter-spacing: 8px; }

  .cover-year {
    position: absolute; right: 40px; top: 408px;
    font-family: "Montserrat", sans-serif; font-weight: 400; font-size: 40px;
    color: rgba(255,255,255,.85);
  }
  .cover-tagline {
    position: absolute; left: 28px; top: 618px;
    font-family: "Montserrat", sans-serif; font-weight: 600; font-size: 11px;
    letter-spacing: 1px; color: var(--purple);
  }
  .cover-web {
    position: absolute; left: 0; right: 0; bottom: 22px; text-align: center;
    font-family: "Open Sans", sans-serif; font-size: 10px; color: rgba(255,255,255,.75);
  }

  .feature {
    position: absolute; left: 34px; width: 300px;
    font-family: "Open Sans", sans-serif; font-size: 12.5px; line-height: 1.55; color: var(--ink);
  }
  .feature--1 { top: 62px; }
  .feature--2 { top: 150px; }
  .feature--3 { top: 290px; }
  .feature--4 { top: 378px; }
  .feature--5 { top: 466px; color: var(--ink-soft); }
  .photo { position: absolute; border-radius: 2px; }
  .photo--device {
    left: 360px; top: 40px; width: 140px; height: 110px;
    background: linear-gradient(135deg, #cfd6e0, #7c8ea6 60%, #3d4c63);
  }
  .photo--instrument {
    left: 360px; top: 280px; width: 140px; height: 100px;
    background: linear-gradient(135deg, #eef1f4, #aab4bf 55%, #6f7a88);
  }
</style>
</head>
<body>
<main class="spread">

  <section class="page page--cover" aria-label="Front cover">
    <svg class="page__art" viewBox="0 0 540 764" aria-hidden="false">
      <defs>
        <linearGradient id="coverPurple" x1="0" y1="0" x2="0" y2="1">
          <stop offset="0" stop-color="#6a3ea6"/>
          <stop offset="1" stop-color="#4a2680"/>
        </linearGradient>
        <radialGradient id="mapGlow" cx="0.5" cy="0.45" r="0.6">
          <stop offset="0" stop-color="#8fb0ec"/>
          <stop offset="0.6" stop-color="#6f7fd0"/>
          <stop offset="1" stop-color="#6a3ea6" stop-opacity="0"/>
        </radialGradient>
      </defs>
      <rect width="540" height="764" fill="var(--paper)"/>
      <path d="M0 0 H540 V340 C430 440 260 500 0 520 Z" fill="url(#coverPurple)"/>
      <g role="img" aria-label="Glowing world map showing a global network of connections">
        <ellipse cx="360" cy="110" rx="240" ry="170" fill="url(#mapGlow)"/>
      </g>
      <path d="M540 320 C440 420 300 480 150 510 C330 500 460 440 540 390 Z" fill="var(--purple-soft)"/>
      <path d="M0 520 C260 500 430 440 540 360 V764 H0 Z" fill="var(--paper-grey)" opacity=".6"/>
      <path d="M0 700 C200 690 400 640 540 560 V610 C400 690 220 720 0 725 Z" fill="var(--black)"/>
      <path d="M0 725 C220 720 400 690 540 610 V764 H0 Z" fill="var(--purple-deep)"/>
    </svg>
    <div class="brand">
      <div class="brand__dot"></div>
      <div class="brand__name">HALVORSEN HEALTH<span>NETWORK</span></div>
    </div>
    <div class="cover-year">2016</div>
    <p class="cover-tagline">SAVING LIVES &amp; REDUCING HEALTH CARE COSTS</p>
    <p class="cover-web">www.halvorsenhealth.example</p>
  </section>

  <section class="page page--inside" aria-label="Inside page">
    <svg class="page__art" viewBox="0 0 540 764">
      <rect width="540" height="764" fill="var(--paper)"/>
      <path d="M0 690 C200 680 400 640 540 580 V620 C400 690 220 715 0 720 Z" fill="var(--swoosh-grey)"/>
      <path d="M0 720 C220 715 400 690 540 620 V764 H0 Z" fill="var(--paper-grey)"/>
    </svg>
    <div class="photo photo--device" role="img" aria-label="Photo of a medical device with tubing"></div>
    <p class="feature feature--1">We help inventors turn promising medical ideas into finished, approved products ready for the US market.</p>
    <p class="feature feature--2">Our team guides design, testing and regulatory filings so your device reaches patients faster.</p>
    <div class="photo photo--instrument" role="img" aria-label="Photo of a slim surgical instrument"></div>
    <p class="feature feature--3">We refine prototypes, source manufacturing partners and prepare every document reviewers expect.</p>
    <p class="feature feature--4">Our distribution network places new products in hospitals and clinics nationwide.</p>
    <p class="feature feature--5">Bring your new products to market with us.</p>
  </section>

</main>
</body>
</html>
```